Create modern and sleek business card for luxury real estate company

We're a "boutique" real estate office looking for a design that gets across a highly modern luxury brand. Blacks and whites are probably the best colors unless we try a silver foil for the logo. I've attached a version of our current logo here. I'd like to swap out the current font on there with Gotham Light Regular.

I'm looking to have one side of the card have the logo with the space for our agents info on the other side.

Target Market(s)

Young professionals in a "luxury" headspace

Industry/Entity Type

Real estate

Contact Information for Business Card

A place for agent name, cell number, website. The slogan "Simply Rethinking Real Estate".

Font styles to use
Other font styles liked:
• Gotham Regular

Colors

Designer to choose only greyscale colors for use in the design.

Requirements
Must have
• Matte black as the background color. Clean lines and use of contrast. A specific design aspect that will use silver foil.
Nice to have
• Up in the air on integrating a QR code
Should not have
• Any houses or other real estate related design (ex: a clip art house)

```html
<!DOCTYPE html>
<html lang="en">
<head>
<meta charset="utf-8">
<title>Meridian Estates — Agent Card</title>
<link rel="stylesheet" href="https://fonts.googleapis.com/css2?family=Montserrat:wght@300;700&family=Dancing+Script:wght@400&display=swap">
<style>
  :root {
    --backdrop: #2c3038;
    --card-black: #141416;
    --card-black-edge: #1d1e21;
    --silver: #c9c9cc;
    --silver-dim: #a9a9ad;
    --white: #ffffff;
  }
  html, body {
    margin: 0;
    width: 1200px;
    height: 1200px;
    overflow: hidden;
    background: var(--backdrop);
  }
  .business-card {
    position: absolute;
    left: 75px;
    top: 300px;
    width: 1050px;
    height: 600px;
    background: linear-gradient(135deg, var(--card-black-edge) 0%, var(--card-black) 55%, var(--card-black-edge) 100%);
    box-shadow: 0 20px 40px rgba(0, 0, 0, 0.45);
    font-family: "Montserrat", "Helvetica Neue", Arial, sans-serif;
  }
  .brand {
    position: absolute;
    left: 38px;
    top: 55px;
    display: flex;
    align-items: center;
    gap: 36px;
  }
  .brand-circle {
    width: 156px;
    height: 156px;
    border: 4px solid var(--silver);
    border-radius: 50%;
    box-sizing: border-box;
  }
  .brand-name {
    color: var(--silver);
    font-weight: 300;
    font-size: 58px;
    line-height: 1.12;
    letter-spacing: 2px;
    text-transform: uppercase;
  }
  .brand-rule {
    height: 3px;
    background: var(--silver);
    margin: 6px 0;
    width: 330px;
  }
  .agent-name {
    position: absolute;
    left: 225px;
    top: 330px;
    margin: 0;
    color: var(--white);
    font-weight: 700;
    font-size: 44px;
    letter-spacing: 0.5px;
  }
  .slogan {
    position: absolute;
    left: 640px;
    top: 225px;
    margin: 0;
    color: var(--silver-dim);
    font-family: "Dancing Script", "Brush Script MT", cursive;
    font-size: 44px;
    line-height: 1.15;
  }
  .slogan span { display: block; }
  .slogan .second-line { margin-left: -30px; }
  .contact {
    position: absolute;
    left: 610px;
    top: 355px;
    margin: 0;
    padding: 0;
    list-style: none;
  }
  .contact-line {
    position: absolute;
    left: 18px;
    top: 36px;
    width: 2px;
    height: 80px;
    background: var(--silver);
  }
  .contact-item {
    position: relative;
    display: flex;
    align-items: center;
    gap: 20px;
    height: 36px;
    margin-bottom: 18px;
    color: var(--silver);
    font-weight: 300;
    font-size: 25px;
    letter-spacing: 1px;
  }
  .contact-icon {
    width: 36px;
    height: 36px;
    flex: none;
  }
</style>
</head>
<body>
  <article class="business-card">
    <header class="brand">
      <div class="brand-circle"></div>
      <div class="brand-name">
        <div>Meridian</div>
        <div class="brand-rule"></div>
        <div>Estates</div>
      </div>
    </header>

    <h1 class="agent-name">Lorem ipsum</h1>

    <p class="slogan">
      <span>“Simply Rethinking</span>
      <span class="second-line">Real Estate”</span>
    </p>

    <ul class="contact">
      <li class="contact-line" aria-hidden="true"></li>
      <li class="contact-item">
        <svg class="contact-icon" viewBox="0 0 36 36" aria-hidden="true">
          <circle cx="18" cy="18" r="16" fill="var(--card-black)" stroke="var(--silver)" stroke-width="2.5"/>
          <path d="M13 11c-1.5 1-2 3-1 5.5 1.5 3.5 4 6 7.5 7.5 2.5 1 4.5.5 5.5-1l-2.5-2.5-2 1.5c-2-1-3.5-2.5-4.5-4.5l1.5-2z" fill="var(--silver)"/>
        </svg>
        <span>234.345.6789</span>
      </li>
      <li class="contact-item">
        <svg class="contact-icon" viewBox="0 0 36 36" aria-hidden="true">
          <circle cx="18" cy="18" r="16" fill="var(--card-black)" stroke="var(--silver)" stroke-width="2.5"/>
          <rect x="10" y="12.5" width="16" height="11" fill="var(--silver)"/>
          <path d="M10 12.5l8 6.5 8-6.5" fill="none" stroke="var(--card-black)" stroke-width="1.5"/>
        </svg>
        <span>Lorem@ipsum.com</span>
      </li>
      <li class="contact-item">
        <svg class="contact-icon" viewBox="0 0 36 36" aria-hidden="true">
          <circle cx="18" cy="18" r="16" fill="var(--card-black)" stroke="var(--silver)" stroke-width="2.5"/>
          <path d="M18 10l6 10h-4.5v6h-3v-6H12z" fill="var(--silver)"/>
        </svg>
        <span>www.Lorem ipsum.com</span>
      </li>
    </ul>
  </article>
</body>
</html>
```